Ulembe Community In Westmarra Website Design

The Ulembe Community In Westmarra is a community organization that promotes the welfare of people of Kenyan descent living in Pennsylvania. We would like a website designed and coded for the community.
Please refer to the attached document for the brief.

Target Market(s)

Kenyan-Americans living in the State of Pennsylvania

Industry/Entity Type

Non-Profit Community Welfare group

Coding

Coded - Design and coding required

Number of Pages Required

1 page

Font styles to use
Other font styles liked:
• Open Sans

Requirements
Must have
• A private members page; calendar feature or a message board; ability to accept payments
Nice to have
• Ability to maintain a members register

```html
<!DOCTYPE html>
<html lang="en">
<head>
<meta charset="utf-8">
<title>Ulembe Community In Westmarra</title>
<link href="https://fonts.googleapis.com/css2?family=Montserrat:wght@400;500;600;700;800&display=swap" rel="stylesheet">
<style>
:root{
  --red:#c8102e;
  --green:#0d6e17;
  --dark:#1b1b1b;
  --text:#333;
  --muted:#555;
  --grey-band:#efefef;
  --pink-band:#fdeeee;
  --green-band:#eafbe6;
  --footer:#f3f3f3;
}
*{box-sizing:border-box;margin:0;padding:0}
html,body{width:1200px;height:4587px;overflow:hidden}
body{font-family:"Montserrat",sans-serif;color:var(--text);background:#fff;position:relative}
.abs{position:absolute}
.photo{position:absolute;display:block}

.topbar{position:absolute;top:0;left:0;width:1200px;height:41px;background:var(--dark);color:#fff;font-size:15px;font-weight:500}
.topbar span{position:absolute;top:12px;display:flex;align-items:center;gap:8px;white-space:nowrap}
.topbar svg{width:16px;height:16px}

.nav{position:absolute;top:41px;left:0;width:1200px;height:85px;background:#fff}
.nav a{position:absolute;top:36px;font-size:13px;color:#333;text-decoration:none;font-weight:500;text-transform:uppercase;white-space:nowrap}
.nav a.active{color:var(--red);font-weight:700;text-decoration:underline}
.brand{position:absolute;left:523px;top:44px;width:150px;height:150px;border-radius:50%;background:#fff;border:2px solid #ddd;display:flex;align-items:center;justify-content:center;text-align:center;z-index:5}
.brand .ring{position:absolute;inset:9px;border-radius:50%;border:1px solid var(--dark)}
.brand b{font-size:13px;font-weight:700;color:var(--dark);line-height:1.3;width:100px}
.nav-line{position:absolute;top:116px;height:1px;background:#999}

.hero{position:absolute;top:126px;left:0;width:1200px;height:570px;overflow:hidden;background:#1c1c1c}
.hero .photo{left:420px;top:0;width:780px;height:570px;background:linear-gradient(90deg,#1c1c1c 0%,#4a3b2e 35%,#7a5a3f 60%,#3f4a2a 100%)}
.hero .welcome{position:absolute;left:105px;top:125px;color:#fff;font-size:24px;font-weight:700}
.hero h1{position:absolute;left:105px;top:160px;color:#fff;font-size:44px;font-weight:800;line-height:56px;text-transform:uppercase;white-space:nowrap}
.hero h1 .r{color:var(--red)}
.hero h1 .g{color:#1aa82a}
.hero p{position:absolute;left:110px;top:284px;width:450px;color:#fff;font-size:14px;line-height:28px}
.btn{position:absolute;display:flex;align-items:center;justify-content:center;border-radius:24px;font-size:14px;font-weight:700;color:#fff;text-transform:uppercase;white-space:nowrap}
.btn.green{background:var(--green)}
.btn.red{background:var(--red)}
.btn.dark{background:var(--dark)}
.btn.outline{background:#fff;border:2px solid var(--green);color:var(--green)}

.band{position:absolute;left:0;width:1200px}
.who{top:656px;height:584px;background:var(--grey-band)}
.sec-title{position:absolute;left:0;width:1200px;text-align:center;font-size:38px;font-weight:600;color:var(--dark);text-transform:uppercase}
.bar{position:absolute;height:5px;width:96px;border-radius:3px;background:linear-gradient(90deg,var(--dark) 0 33%,var(--red) 33% 66%,var(--green) 66%)}
.bar.center{left:552px}
h2.left{position:absolute;font-size:38px;font-weight:600;color:var(--dark);line-height:48px;text-transform:uppercase}
.body-p{position:absolute;font-size:14px;line-height:28px;color:var(--muted)}

.card{position:absolute;top:1418px;width:312px;height:344px;border:2px solid var(--green);border-radius:8px;background:#fff;overflow:hidden}
.card.hover{box-shadow:-9px 9px 0 var(--red)}
.card .photo{left:0;top:0;width:100%;height:189px}
.date{position:absolute;top:150px;right:12px;width:70px;height:70px;border-radius:50%;background:var(--red);border:3px solid #fff;color:#fff;text-align:center;font-weight:700;font-size:22px;line-height:1;padding-top:13px}
.date small{display:block;font-size:12px;margin-top:3px}
.card h3{position:absolute;left:20px;top:216px;font-size:18px;font-weight:600;color:var(--dark)}
.card p{position:absolute;left:20px;top:252px;width:270px;font-size:13px;line-height:26px;color:var(--muted)}
.card .time{position:absolute;left:20px;top:314px;font-size:13px;font-weight:600;color:var(--dark);display:flex;align-items:center;gap:6px}

.initiatives{top:1931px;height:757px;background:var(--pink-band)}
.arrow{position:absolute;width:54px;height:54px;border-radius:50%;display:flex;align-items:center;justify-content:center}
.arrow.prev{left:28px;top:2321px;border:2px solid var(--dark);background:#fff}
.arrow.next{left:1105px;top:2321px;background:var(--red)}
.dots{position:absolute;top:2570px;left:545px;display:flex;gap:22px;align-items:center}
.dots i{width:11px;height:11px;border-radius:50%;background:#777;display:block}
.dots i.on{width:20px;height:20px;background:var(--red);border:3px solid #fff;box-shadow:0 0 0 2px var(--red)}

.tile{position:absolute;width:312px;height:310px;border-radius:18px;overflow:hidden}
.tile.featured{background:#a3121f;color:#fff;text-align:center;font-size:14px;line-height:28px;padding:70px 24px 0}
.tile.featured .dot{width:32px;height:32px;border-radius:50%;border:3px solid #fff;margin:0 auto 14px}

.fund{top:3578px;height:646px;background:var(--green-band)}

.footer{top:4224px;height:363px;background:var(--footer)}
.footer h4{position:absolute;font-size:20px;font-weight:600;color:var(--dark);text-transform:uppercase}
.footer ul{position:absolute;list-style:none;font-size:14px;line-height:27px;color:#444}
.footer ul li.active{color:var(--green);font-weight:700;text-decoration:underline}
.contact li{display:flex;align-items:center;gap:10px}
.contact .ico{width:22px;height:22px;border-radius:50%;background:var(--green);flex:none}
.payments{position:absolute;left:100px;top:4444px;width:210px;display:flex;flex-wrap:wrap;justify-content:center;gap:8px 10px}
.pay{font-size:11px;font-weight:700;color:var(--dark);white-space:nowrap;line-height:16px}
.copy{position:absolute;left:0;width:1080px;text-align:right;top:4553px;font-size:13px;color:#333}
.rule{position:absolute;left:110px;top:4528px;width:975px;height:1px;background:#777}
</style>
</head>
<body>

<header class="topbar">
  <span style="left:110px"><svg viewBox="0 0 24 24" fill="none" stroke="#fff" stroke-width="2"><path d="M5 3h4l2 5-3 2a12 12 0 0 0 6 6l2-3 5 2v4a2 2 0 0 1-2 2A17 17 0 0 1 3 5a2 2 0 0 1 2-2z"/></svg>+1 555 010 2040</span>
  <span style="left:282px"><svg viewBox="0 0 24 24" fill="none" stroke="#fff" stroke-width="2"><rect x="3" y="5" width="18" height="14" rx="1"/><path d="M3 6l9 7 9-7"/></svg>info@uciw.org</span>
  <span style="left:684px"><svg viewBox="0 0 24 24" fill="none" stroke="#fff" stroke-width="2"><circle cx="12" cy="12" r="9"/></svg>Follow Us Pictora</span>
  <span style="left:893px"><svg viewBox="0 0 24 24" fill="none" stroke="#fff" stroke-width="2"><rect x="3" y="5" width="18" height="16" rx="1"/><path d="M3 10h18M8 3v4M16 3v4"/></svg>Event</span>
  <span style="left:993px"><svg viewBox="0 0 24 24" fill="none" stroke="#fff" stroke-width="2"><circle cx="12" cy="8" r="4"/><path d="M4 21c1-5 15-5 16 0"/></svg>Sign Up</span>
</header>

<nav class="nav">
  <a class="active" style="left:134px">Home</a>
  <a style="left:226px">About Us</a>
  <a style="left:350px">Our Initiatives</a>
  <a style="left:729px">Purposes Of Fund Raising</a>
  <a style="left:975px">Contact Us</a>
  <div class="nav-line" style="left:500px;width:23px"></div>
  <div class="nav-line" style="left:673px;width:23px"></div>
</nav>
<div class="brand"><div class="ring"></div><b>Ulembe Community In Westmarra</b></div>

<section class="hero">
  <div class="photo" role="img" aria-label="Smiling Kenyan-American community members"></div>
  <div class="welcome">WELCOME TO</div>
  <h1><span class="r">Ulembe</span> Community<br>In <span class="g">Westmarra</span></h1>
  <p>Lorem Ipsum is simply dummy text of the printing and typesetting industry. Lorem Ipsum has been the industry's standard dummy text ever since the 1500s,</p>
  <div class="btn green" style="left:111px;top:387px;width:156px;height:45px">Get Started</div>
</section>

<section class="band who">
  <svg class="abs" style="left:0;top:0" width="1200" height="60" viewBox="0 0 1200 60"><path d="M0 0h1200v30C900 80 500 60 0 0z" fill="#1c1c1c"/></svg>
  <h2 class="left" style="left:110px;top:106px">Who Is The Ulembe<br>Community In<br>Westmarra</h2>
  <div class="bar" style="left:110px;top:266px"></div>
  <p class="body-p" style="left:110px;top:292px;width:440px">Lorem Ipsum is simply dummy text of the printing and typesetting industry. Lorem Ipsum has been the industry's standard dummy text ever since the 1500s, when an unknown printer took a galley of type and scrambled it to make a type</p>
  <div class="btn dark" style="left:111px;top:424px;width:152px;height:44px">Read More</div>
  <div class="photo" role="img" aria-label="Crowd of community members gathered outdoors" style="left:643px;top:93px;width:400px;height:400px;border-radius:50%;border:4px solid var(--green);background:radial-gradient(circle,#7a5a3c,#3f3022)"></div>
  <svg class="abs" style="left:0;top:524px" width="1200" height="60" viewBox="0 0 1200 60"><path d="M0 60h1200V30C800 60 300 70 0 30z" fill="#fff"/></svg>
</section>

<h2 class="sec-title" style="top:1296px">Upcoming Events</h2>
<div class="bar center" style="top:1360px"></div>

<article class="card hover" style="left:108px">
  <div class="photo" role="img" aria-label="Volunteer in red cap at a community event" style="background:linear-gradient(135deg,#b84a3a,#5d3a2a)"></div>
  <div class="date">10<small>SEP</small></div>
  <h3>Lorem Ipsum</h3>
  <p>September 10 -  simply dummy text of the printing and typesetting industry.</p>
  <div class="time"><svg width="14" height="14" viewBox="0 0 24 24" fill="none" stroke="#222" stroke-width="2"><circle cx="12" cy="12" r="9"/><path d="M12 7v5l3 2"/></svg>8.00 AM - 1:00 PM</div>
</article>
<article class="card" style="left:443px">
  <div class="photo" role="img" aria-label="Group smiling beside a red bus" style="background:linear-gradient(135deg,#7a3a36,#a82a2a)"></div>
  <div class="date">16<small>SEP</small></div>
  <h3>Lorem Ipsum</h3>
  <p>September 16 -  simply dummy text of the printing and typesetting industry.</p>
  <div class="time"><svg width="14" height="14" viewBox="0 0 24 24" fill="none" stroke="#222" stroke-width="2"><circle cx="12" cy="12" r="9"/><path d="M12 7v5l3 2"/></svg>8.00 AM - 1:00 PM</div>
</article>
<article class="card" style="left:778px">
  <div class="photo" role="img" aria-label="Dancers in traditional dress at a festival" style="background:linear-gradient(135deg,#c07a2e,#6a3a1c)"></div>
  <div class="date">19<small>SEP</small></div>
  <h3>Lorem Ipsum</h3>
  <p>September 19 -  simply dummy text of the printing and typesetting industry.</p>
  <div class="time"><svg width="14" height="14" viewBox="0 0 24 24" fill="none" stroke="#222" stroke-width="2"><circle cx="12" cy="12" r="9"/><path d="M12 7v5l3 2"/></svg>8.00 AM - 1:00 PM</div>
</article>
<div class="btn outline" style="left:503px;top:1814px;width:190px;height:46px">View All Events</div>

<section class="band initiatives"></section>
<h2 class="sec-title" style="top:2048px">Our Initiatives</h2>
<div class="bar center" style="top:2112px"></div>
<div class="photo" role="img" aria-label="Drummer in traditional beads and headdress" style="left:112px;top:2163px;width:463px;height:370px;border-radius:26px;background:linear-gradient(135deg,#3b6fa0,#6a4a2e 55%,#2a1e16)"></div>
<h3 class="abs" style="left:618px;top:2183px;font-size:26px;font-weight:600;color:var(--dark)">CULTURAL EVENTS</h3>
<p class="body-p" style="left:619px;top:2231px;width:440px">Lorem Ipsum is simply dummy text of the printing and typesetting industry. Lorem Ipsum has been the industry's standard dummy text ever since the 1500s, when an unknown printer took a galley of type and scrambled it to make a type specimen book. It has survived not only five centuries, but also the leap into electronic typesetting, remaining essentially unchanged.</p>
<div class="btn red" style="left:618px;top:2463px;width:154px;height:46px">Read More</div>
<div class="arrow prev"><svg width="22" height="22" viewBox="0 0 24 24" fill="none" stroke="#222" stroke-width="3"><path d="M15 5l-7 7 7 7"/></svg></div>
<div class="arrow next"><svg width="22" height="22" viewBox="0 0 24 24" fill="none" stroke="#fff" stroke-width="3"><path d="M9 5l7 7-7 7"/></svg></div>
<div class="dots"><i></i><i class="on"></i><i></i><i></i></div>

<h2 class="sec-title" style="top:2748px">Follow Us On Pictora</h2>
<div class="bar center" style="top:2814px"></div>
<div class="tile featured" style="left:110px;top:2875px"><div class="dot"></div><b>Lorem Ipsum is simply dummy</b><br>Lorem Ipsum is simply dummy text of the printing and typesetting industry. Lorem Ipsum has been the industry's standard dummy text</div>
<div class="tile photo" role="img" aria-label="Women in colourful headwraps and beads" style="left:443px;top:2875px;background:linear-gradient(135deg,#2e7a6a,#c8962e,#6a3a22)"></div>
<div class="tile photo" role="img" aria-label="Smiling child with face paint" style="left:776px;top:2875px;background:linear-gradient(135deg,#8a6a48,#4a3424)"></div>
<div class="tile photo" role="img" aria-label="Two women in patterned traditional cloth" style="left:110px;top:3206px;background:linear-gradient(135deg,#2a1e18,#b8502a,#c23a2a)"></div>
<div class="tile photo" role="img" aria-label="Laughing woman with braided hair" style="left:443px;top:3206px;background:linear-gradient(135deg,#6a4a30,#3a2618)"></div>
<div class="tile photo" role="img" aria-label="Large crowd before a thatched hut" style="left:776px;top:3206px;background:linear-gradient(180deg,#8ab0c8,#7a5a3a 40%,#c07a2e)"></div>

<section class="band fund">
  <h2 class="left" style="left:110px;top:160px">Purposes Of<br>Fund Raising</h2>
  <div class="bar" style="left:110px;top:270px"></div>
  <p class="body-p" style="left:114px;top:304px;width:440px">Lorem Ipsum is simply dummy text of the printing and typesetting industry. Lorem Ipsum has been the industry's standard dummy text ever since the 1500s, when an unknown printer took a galley of type and scrambled it to make a type specimen book.</p>
  <div class="btn green" style="left:114px;top:474px;width:152px;height:44px">Donate Us</div>
  <div class="photo" role="img" aria-label="Men in red shukas walking through grassland" style="left:619px;top:133px;width:445px;height:397px;border-radius:22px;background:linear-gradient(180deg,#5a8ac0,#c4a070 55%,#a8322a)"></div>
</section>

<footer class="band footer">
  <div class="abs" style="left:125px;top:60px;width:148px;height:148px;border-radius:50%;border:2px solid #333;display:flex;align-items:center;justify-content:center;text-align:center;font-size:13px;font-weight:700;color:var(--dark);padding:18px;background:var(--footer)">Ulembe Community In Westmarra</div>
  <h4 style="left:384px;top:48px">Main Links</h4>
  <ul style="left:388px;top:90px"><li class="active">Home</li><li>About Us</li><li>Our Initiatives</li><li>Purposes Of Fund Raising</li><li>Contact Us</li></ul>
  <h4 style="left:643px;top:48px">Other Links</h4>
  <ul style="left:644px;top:90px"><li>Customer Support</li><li>Privacy Policy</li><li>Terms And Conditions</li></ul>
  <h4 style="left:900px;top:48px">Contact Info</h4>
  <ul class="contact" style="left:903px;top:90px;line-height:32px"><li><span class="ico"></span>+1 555 010 2040</li><li><span class="ico"></span>info@uciw.org</li><li><span class="ico"></span>3306 Lorem Ipsum Is</li><li style="padding-left:32px">Simply Dummy Text</li></ul>
</footer>
<div class="payments">
  <span class="pay">Tarnby Bank</span>
  <span class="pay">Kivuli Pay</span>
  <span class="pay">Orvessa</span>
  <span class="pay">Bank Wire</span>
  <span class="pay">Direct Debit</span>
</div>
<div class="abs" style="left:112px;top:4536px;width:34px;height:34px;border-radius:50%;border:2px solid #222"></div>
<div class="rule"></div>
<div class="copy">© 2024  The Ulembe Community In Westmarra I All Rights Reserved</div>

</body>
</html>
```